Natural Cosmetics need a Packaging Design

We need a PACKAGING design for labels on hand/body wash bottles and soap paper boxes.
We target at high end markets.
We expect a contemporary and trendy design.
We don't need a separate logo. The brand name "Va Mirel" acts as the logo.
We want a modern and classic font for "Va Mirel".
Please see attached pictures for packaging samples.

Industry/Entity Type

Cosmetics

Requirements
Should not have
• a separate logo from the brand name

```html
<!DOCTYPE html>
<html lang="en">
<head>
<meta charset="utf-8">
<title>Va Mirel — Soap Box Packaging</title>
<link rel="stylesheet" href="https://fonts.googleapis.com/css2?family=Open+Sans:wght@400;600&display=swap">
<style>
  :root {
    --stage: #e3e4e5;
    --ink: #1b1b1b;
    --paper: #ffffff;
    --teal: #5fb3ba;
    --teal-deep: #4a9ea6;
    --sky: #9fd0ee;
    --lemon: #f4f08f;
    --blush: #eeb1c4;
    --night: #141414;
  }
  * { box-sizing: border-box; margin: 0; padding: 0; }
  html, body {
    width: 1200px; height: 1000px; overflow: hidden;
    background: var(--stage);
    font-family: "Open Sans", Arial, sans-serif;
    color: var(--ink);
  }
  .box-net {
    position: absolute;
    left: 170px; top: 190px;
    width: 860px; height: 620px;
  }
  .panel { position: absolute; overflow: hidden; }

  /* side end panel */
  .panel--side {
    left: 0; top: 0; width: 150px; height: 440px;
    background: var(--night);
  }
  .panel--side .side-pattern {
    position: absolute; inset: 0;
    background: linear-gradient(160deg, var(--night) 0%, #1e3a40 55%, var(--night) 100%);
  }
  .panel--side .panel-copy {
    position: absolute; left: 50%; top: 50%;
    width: 360px;
    transform: translate(-50%, -50%) rotate(90deg);
    color: var(--paper);
    font-size: 15px; line-height: 1.45; text-align: center;
  }

  /* top lid panel */
  .panel--lid {
    left: 150px; top: 0; width: 710px; height: 440px;
  }
  .lid-pattern {
    position: absolute; inset: 0;
    background:
      linear-gradient(120deg,
        var(--night) 0%, var(--night) 14%,
        var(--lemon) 14%, var(--lemon) 34%,
        var(--paper) 34%, var(--paper) 56%,
        var(--blush) 56%, var(--blush) 72%,
        var(--lemon) 72%, var(--lemon) 84%,
        var(--teal) 84%, var(--teal) 100%);
  }
  .lid-label {
    position: absolute;
    left: 110px; top: 80px; width: 500px; height: 270px;
  }
  .brand {
    position: absolute; left: 0; right: 0; top: 95px;
    text-align: center;
  }
  .brand__name {
    font-size: 84px; font-weight: 600; letter-spacing: 1px;
    line-height: 1; color: var(--ink);
  }
  .brand__origin {
    margin-top: 18px;
    font-size: 17px; font-weight: 400; letter-spacing: 1.5px;
    color: var(--ink);
  }

  /* front panel */
  .panel--front {
    left: 150px; top: 440px; width: 710px; height: 180px;
    background: var(--teal);
  }
  .front-pattern {
    position: absolute; inset: 0;
    background: linear-gradient(90deg, var(--teal-deep) 0%, var(--teal) 50%, var(--teal-deep) 100%);
  }
  .panel--front .panel-copy {
    position: absolute; left: 250px; top: 62px;
    font-size: 17px; line-height: 1.4; color: var(--ink);
  }
</style>
</head>
<body>
  <main class="box-net">
    <section class="panel panel--side">
      <div class="side-pattern" role="img" aria-label="Black end panel with sky-blue brush-dab pattern"></div>
      <p class="panel-copy">Lorem ipsum dolor sit amet,<br>consectetur adipiscing elit.</p>
    </section>

    <section class="panel panel--lid">
      <div class="lid-pattern" role="img" aria-label="Memphis-style brush-stroke pattern in black, lemon yellow, blush pink, sky blue and teal with black dashes and dots"></div>
      <svg class="lid-label" viewBox="0 0 500 270" aria-hidden="true">
        <path d="M30 40 C90 10 200 22 280 14 C360 8 440 20 480 44 C496 90 488 170 470 220 C400 250 300 244 220 252 C140 258 70 250 26 226 C10 170 14 90 30 40 Z" fill="var(--paper)"/>
      </svg>
      <div class="brand">
        <h1 class="brand__name">Va Mirel</h1>
        <p class="brand__origin">MADE IN FRANCE</p>
      </div>
    </section>

    <section class="panel panel--front">
      <div class="front-pattern" role="img" aria-label="Teal panel with scattered black brush-dab pattern"></div>
      <p class="panel-copy">Lorem ipsum dolor sit amet,<br>consectetur adipiscing elit.</p>
    </section>
  </main>
</body>
</html>
```